Business Cards

The name of our firm is "Bayfield Insurance adjusters"
We separate ourselves from all other public adjusters because most of us worked for the insurance companies so we understand their games.
As Insurance adjusters we represent the Insured, not the insurance companies. Our # 1 priority is to handle the entire claim process as seamless as possible on behalf of the homeowner/business owner so they don't have to deal with the hassles and headaches. Just as the logo your team designed, I want the cards to stand out from everyone elses. I also want the cards to help better understand our services and Value on hiring us and value that we can offer.
I uploaded the logo whenever I created the project. I don't see an option on re uploading the logo anywhere. Any advise??

```html
<!DOCTYPE html>
<html lang="en">
<head>
<meta charset="utf-8">
<title>Bayfield Insurance Adjusters – Business Card</title>
<link rel="stylesheet" href="https://fonts.googleapis.com/css2?family=Josefin+Sans:wght@400;600;700&display=swap">
<style>
  :root {
    --bg: #9a9c9e;
    --card-dark: #1f1f1f;
    --card-dark-edge: #1a1a1a;
    --card-light: #ffffff;
    --brand-blue: #0e6199;
    --brand-blue-light: #1478b8;
    --ink: #1c1c1c;
    --ink-soft: #3a3a3a;
    --mark-dark: #4a4a4a;
  }
  * { box-sizing: border-box; margin: 0; padding: 0; }
  html, body {
    width: 1187px;
    height: 1200px;
    overflow: hidden;
    background: var(--bg);
    font-family: "Josefin Sans", sans-serif;
  }
  .canvas { position: relative; width: 1187px; height: 1200px; }

  .card { position: absolute; overflow: hidden; }

  /* Front */
  .card-front {
    left: 216px; top: 119px; width: 756px; height: 436px;
    background: radial-gradient(ellipse at 50% 45%, #262626 0%, var(--card-dark) 55%, var(--card-dark-edge) 100%);
  }
  .front-brand {
    position: absolute; left: 0; right: 0; top: 180px;
    text-align: center;
    color: var(--mark-dark);
    font-weight: 700;
    font-size: 34px;
    line-height: 40px;
    letter-spacing: 1px;
    text-transform: uppercase;
  }

  /* Back */
  .card-back {
    left: 213px; top: 641px; width: 763px; height: 440px;
    background: var(--card-light);
  }
  .back-brand {
    position: absolute; left: 88px; top: 168px; width: 240px;
    text-align: center;
    color: var(--brand-blue);
    font-weight: 700;
    font-size: 26px;
    line-height: 32px;
    text-transform: uppercase;
  }
  .divider {
    position: absolute; left: 380px; top: 124px;
    width: 2px; height: 192px;
    background: var(--ink);
  }
  .divider-accent {
    position: absolute; left: 379px; top: 165px;
    width: 4px; height: 108px;
    background: var(--brand-blue);
  }
  .person-name {
    position: absolute; left: 422px; top: 118px;
    color: var(--brand-blue);
    font-weight: 700;
    font-size: 30px;
    letter-spacing: 1px;
    text-transform: uppercase;
  }
  .person-role {
    position: absolute; left: 422px; top: 157px;
    color: var(--ink-soft);
    font-weight: 400;
    font-size: 18px;
    letter-spacing: 1px;
  }
  .contacts {
    position: absolute; left: 422px; top: 235px;
    list-style: none;
  }
  .contact {
    display: flex; align-items: center;
    height: 31px;
    color: var(--ink);
    font-size: 19px;
    letter-spacing: 2px;
  }
  .contact svg { width: 16px; height: 16px; margin-right: 10px; fill: var(--brand-blue); flex: none; }
  .back-band {
    position: absolute; left: 0; right: 0; bottom: 0; height: 17px;
    background: linear-gradient(90deg, var(--brand-blue), var(--brand-blue-light));
    border-top: 2px solid var(--ink);
  }
</style>
</head>
<body>
<main class="canvas">
  <section class="card card-front" aria-label="Card front">
    <p class="front-brand">Bayfield<br>Insurance Adjusters</p>
  </section>

  <section class="card card-back" aria-label="Card back">
    <p class="back-brand">Bayfield<br>Insurance Adjusters</p>
    <span class="divider"></span>
    <span class="divider-accent"></span>
    <h1 class="person-name">Marcus Whitfield</h1>
    <p class="person-role">Founder &amp; CEO</p>
    <ul class="contacts">
      <li class="contact">
        <svg viewBox="0 0 24 24" aria-hidden="true"><path d="M6.6 10.8a15.1 15.1 0 0 0 6.6 6.6l2.2-2.2c.3-.3.7-.4 1-.2 1.1.4 2.3.6 3.6.6.6 0 1 .4 1 1V20c0 .6-.4 1-1 1C10.6 21 3 13.4 3 4c0-.6.4-1 1-1h3.5c.6 0 1 .4 1 1 0 1.3.2 2.5.6 3.6.1.3 0 .7-.2 1l-2.3 2.2z"/></svg>
        321-555-0147
      </li>
      <li class="contact">
        <svg viewBox="0 0 24 24" aria-hidden="true"><path d="M2 5h20v14H2z M4 7v.5l8 5 8-5V7z" fill-rule="evenodd"/></svg>
        info@yourwebsite.com
      </li>
      <li class="contact">
        <svg viewBox="0 0 24 24" aria-hidden="true"><circle cx="12" cy="12" r="10"/></svg>
        www.yourwebsite.com
      </li>
    </ul>
    <span class="back-band"></span>
  </section>
</main>
</body>
</html>
```